VelmoraTrade.com -Ecommerce Website for Luxury Products

This will be an ecommerce site. A website portal that will allow both consumers to enter one way and see specific purchase options and businesses to enter via a different link that allows B2B to see their specific options once logged into. B2C can purchase both as a guest/or after account is setup. B2B must be approved to set up account. This is front end website project. Back-end integration is separate. Will be hosted on Serventa with a domain registration held at PortaVance. Additional website concept/idea/synergy can be found from sister site-KRWEHospitality.com

```html
<!DOCTYPE html>
<html lang="en">
<head>
<meta charset="utf-8">
<title>Velmora Trade — Purveyors of Luxury Lifestyle Accoutrements</title>
<link rel="stylesheet" href="https://fonts.googleapis.com/css2?family=Playfair+Display:ital,wght@0,400;0,600;0,700;1,700&family=Montserrat:wght@400;500;600&display=swap">
<style>
:root{
  --ink:#0d0d0d;
  --night:#141414;
  --cream:#f4f1ea;
  --white:#ffffff;
  --gold:#c9a96a;
  --gold-band:#c8ad79;
  --muted:#6b6b6b;
  --serif:"Playfair Display", Georgia, serif;
  --sans:"Montserrat", Arial, sans-serif;
}
*{box-sizing:border-box;margin:0;padding:0}
html,body{width:1200px;height:2652px;overflow:hidden}
body{font-family:var(--sans);color:var(--ink);background:var(--white)}
.crown{display:block;margin:0 auto}

/* Hero */
.hero{position:relative;height:620px;background:radial-gradient(ellipse at 50% 45%,#4a4035 0%,#22201d 45%,#0c0c0c 100%);color:var(--white)}
.hero-scene{position:absolute;inset:0}
.topbar{position:absolute;top:0;left:0;right:0;height:110px;display:flex;justify-content:space-between;align-items:flex-start;padding:28px 60px}
.brand{display:flex;align-items:center;gap:14px}
.brand-mark{width:40px;height:40px;border:1px solid var(--white)}
.brand-name{font-family:var(--serif);font-size:26px;letter-spacing:1px}
.brand-tag{font-size:9px;letter-spacing:1px;margin-top:4px;color:var(--gold)}
.nav{display:flex;gap:30px;font-size:11px;letter-spacing:1px;text-transform:uppercase;margin-top:14px}
.nav a{color:var(--white);text-decoration:none}
.nav a.current{color:var(--gold)}
.hero-copy{position:absolute;top:300px;left:0;right:0;text-align:center}
.hero-title{font-family:var(--serif);font-weight:400;font-size:62px;line-height:1.05}
.hero-title em{font-weight:700}
.hero-sub{font-size:17px;margin-top:14px;opacity:.9}
.hero-actions{display:flex;justify-content:center;gap:20px;margin-top:26px}
.btn{display:inline-block;font-size:12px;font-weight:600;letter-spacing:1px;text-transform:uppercase;padding:12px 22px;text-decoration:none}
.btn-gold{background:var(--gold);color:var(--ink)}
.btn-outline{border:1px solid var(--white);color:var(--white)}
.btn-dark{background:var(--ink);color:var(--white);border-radius:4px}

/* Collections */
.collections{height:710px;background:var(--cream);padding-top:62px;text-align:center}
.section-title{font-family:var(--serif);font-weight:700;font-size:42px;margin-top:6px}
.cards{display:flex;justify-content:center;gap:24px;margin-top:52px}
.card{width:196px;height:300px;background:var(--white);padding:18px 16px;box-shadow:0 2px 10px rgba(0,0,0,.06)}
.card-media{height:126px}
.card-title{font-family:var(--serif);font-weight:700;font-size:15px;margin-top:18px}
.card-text{font-size:10px;color:var(--muted);line-height:1.5;margin-top:10px;height:45px}
.card-link{display:inline-block;margin-top:14px;border:1px solid var(--gold);color:var(--gold);font-size:10px;letter-spacing:1px;padding:8px 14px;text-transform:uppercase}
.collections .btn-dark{margin-top:52px}

/* About */
.about{display:flex;height:350px;background:var(--ink);color:var(--white)}
.about-media{width:640px;background:linear-gradient(100deg,#d8d2c6 0%,#a89a83 45%,#3e3a35 100%)}
.about-copy{padding:70px 60px 0 40px;width:560px;position:relative}
.about-title{font-family:var(--serif);font-weight:700;font-size:40px}
.about-text{font-size:11px;line-height:1.6;margin-top:10px;opacity:.9}
.about-copy .crown{position:absolute;left:-60px;top:150px}
.about .btn-gold{margin-top:26px;font-size:10px;padding:10px 16px;border-radius:3px}

/* Partner */
.partner{height:400px;background:var(--gold-band);text-align:center;padding-top:58px}
.partner-title{font-family:var(--serif);font-weight:700;font-style:italic;font-size:58px;margin-top:6px}
.partner-title span{font-style:normal;font-weight:400}
.partner-text{font-size:16px;line-height:1.5;width:700px;margin:12px auto 0}
.partner .btn-dark{margin-top:22px}

/* Showcase */
.showcase{height:320px;background:var(--white);text-align:center;padding-top:94px}
.showcase .section-title{font-size:36px}
.logo-row{display:flex;justify-content:center;gap:160px;margin-top:30px;font-family:var(--serif);font-size:14px}

/* Footer */
.footer{height:252px;background:var(--night);color:var(--white);padding:40px 180px 0;position:relative}
.footer-cols{display:flex;justify-content:space-between}
.footer h4{font-size:12px;font-weight:600;margin-bottom:10px}
.footer li{list-style:none;font-size:10px;line-height:1.7;opacity:.85}
.footer-col{width:260px}
.footer-col-narrow{width:120px}
.copyright{position:absolute;bottom:20px;left:0;right:0;text-align:center;font-size:9px;opacity:.6}
</style>
</head>
<body>
<header class="hero">
  <div class="hero-scene" role="img" aria-label="Dimly lit luxury boutique interior with illuminated display cases of handbags and goods"></div>
  <div class="topbar">
    <div>
      <div class="brand"><span class="brand-mark"></span><span class="brand-name">VELMORA TRADE</span></div>
      <div class="brand-tag">Purveyors of Luxury Lifestyle Accoutrements</div>
    </div>
    <nav class="nav">
      <a class="current" href="#">Home</a><a href="#">About</a><a href="#">Collections</a><a href="#">Wholesale</a><a href="#">Partners</a><a href="#">Contact</a>
    </nav>
  </div>
  <div class="hero-copy">
    <h1 class="hero-title">Purveyors of <em>Luxury<br>Lifestyle</em> Accoutrements</h1>
    <p class="hero-sub">Curating limited edition luxury items is fun… but one of a kind is LUXE.</p>
    <div class="hero-actions"><a class="btn btn-gold" href="#">Shop Now</a><a class="btn btn-outline" href="#">Wholesale Login</a></div>
  </div>
</header>

<section class="collections">
  <svg class="crown" width="26" height="18" viewBox="0 0 26 18"><path d="M2 16h22L22 4l-5 5-4-8-4 8-5-5z" fill="#0d0d0d"/></svg>
  <h2 class="section-title">Our Collections</h2>
  <div class="cards">
    <article class="card">
      <div class="card-media" role="img" aria-label="Cigar accessories on dark leather" style="background:linear-gradient(135deg,#5a3a22,#1a120c)"></div>
      <h3 class="card-title">Cigar Accessories</h3>
      <p class="card-text">Handcrafted cutters, lighters and humidors chosen for the discerning aficionado.</p>
      <span class="card-link">View Collection</span>
    </article>
    <article class="card">
      <div class="card-media" role="img" aria-label="Fragrance bottles and oils" style="background:linear-gradient(135deg,#c59a55,#3b2a17)"></div>
      <h3 class="card-title">Oils &amp; Fragrances</h3>
      <p class="card-text">Rare essential oils and signature fragrances blended in small artisan batches.</p>
      <span class="card-link">View Collection</span>
    </article>
    <article class="card">
      <div class="card-media" role="img" aria-label="Tailored suit attire and accessories" style="background:linear-gradient(135deg,#2b3550,#0c1020)"></div>
      <h3 class="card-title">Attire &amp; Accessories</h3>
      <p class="card-text">Tailored clothing, leather goods and fine accessories for every occasion.</p>
      <span class="card-link">View Collection</span>
    </article>
    <article class="card">
      <div class="card-media" role="img" aria-label="Limited edition luxury pieces" style="background:linear-gradient(135deg,#8a6a3c,#1c1610)"></div>
      <h3 class="card-title">Limited Editions</h3>
      <p class="card-text">One of a kind treasures and collectible pieces available for a short time only.</p>
      <span class="card-link">View Collection</span>
    </article>
  </div>
  <a class="btn btn-dark" href="#">Explore All</a>
</section>

<section class="about">
  <div class="about-media" role="img" aria-label="Man in a tailored suit standing in a luxury boutique"></div>
  <div class="about-copy">
    <svg class="crown" width="26" height="18" viewBox="0 0 26 18"><path d="M2 16h22L22 4l-5 5-4-8-4 8-5-5z" fill="#ffffff"/></svg>
    <h2 class="about-title">About Velmora Trade</h2>
    <p class="about-text">Elegant, confident and refined, Velmora Trade speaks to both the discerning consumer and the sophisticated business owner. Our team curates luxury accoutrements for personal indulgence and wholesale partnerships, supported by a product quality promise and devotion. As a division of our hospitality group, we create experiences that elevate everyday moments.</p>
    <a class="btn btn-gold" href="#">Learn More</a>
  </div>
</section>

<section class="partner">
  <svg class="crown" width="34" height="22" viewBox="0 0 26 18"><path d="M2 16h22L22 4l-5 5-4-8-4 8-5-5z" fill="#0d0d0d"/></svg>
  <h2 class="partner-title">Become <span>a Partner</span></h2>
  <p class="partner-text">Elevate your lounge and impress your clientele with our curated selection of luxury lifestyle accoutrements. Register for our wholesale portal to access exclusive collections, partner pricing and dedicated support.</p>
  <a class="btn btn-dark" href="#">Wholesale Portal</a>
</section>

<section class="showcase">
  <svg class="crown" width="26" height="18" viewBox="0 0 26 18"><path d="M2 16h22L22 4l-5 5-4-8-4 8-5-5z" fill="#0d0d0d"/></svg>
  <h2 class="section-title">Partner Showcase</h2>
  <div class="logo-row"><span>Lounge A</span><span>Club B</span><span>Resort C</span><span>Bar D</span></div>
</section>

<footer class="footer">
  <div class="footer-cols">
    <div class="footer-col"><h4>Navigate</h4><ul><li>Home</li><li>About</li><li>Collections</li><li>Wholesale</li><li>Partners</li><li>Contact</li></ul></div>
    <div class="footer-col"><h4>Contact</h4><ul><li>Email: info@velmoratrade.com</li><li>Phone: +1 (555) 014-2290</li><li>Location: Global Headquarters</li></ul></div>
    <div class="footer-col footer-col-narrow"><h4>Follow Us</h4></div>
  </div>
  <p class="copyright">© 2024 Velmora Trade. All rights reserved.</p>
</footer>
</body>
</html>
```